Integrative Medical Practice Website Redo

I am needing to have our current website redesigned to make it a responsive website to work on smartphones.
Current website
www.brightoakfm.com
Here are several examples of what I am looking for
https://www.corvanhealth.com/
I am wanting a popup for a newsletter signup
Looking for a very professional, clean, simple, minimalist, bold well designed website
Colors would ideally be greens and blues, cool tones, muted colors, or graytones like:
https://journeybright.org/
Several other clean design examples
http://7harborsrenton.com/
http://www.belvomedical.com/
http://sunpathyouth.com/
http://yourcellduke.com/
I would like the top navigation bar to be able to slide down while browsing site
We are also needing to add several features that are not on our current website:
Questionnaire buttons
Are you toxic questionnaire?
Take our hormone quiz to find out if hormones are affecting your health.
online scheduling option for:
nutrition counselling
testing like body composition, basal metabolic rate, CIMT, breast thermography, VO2 Max testing, Vita Trace
Therapies like whole body vibration, infrared sauna, Exercise with oxygen, hyperbaric oxygen, spinal decompression
Need to have separate page for different services and split up services into:
Consults/Office Visits, Testing, Therapies, Procedures
Need to have a button link to patient portal
Needs to have online store
Need to add navigation button "Start Here"
Need a spot for a video on practice summary
Newsletter signup to collect emails
Testimonials from linkpage
Blog that posts can be shared with social media
Password protected patient access that can integrate into crate.net ideally
Modules for programs online classes/videos
I have attached stock images that you can use, but feel free to find others to use.
I have also attached a copy of our current brochure that shows an overview of the practice
Target Market(s)
Health conscious people of all ages looking for a family medicine doctor
Industry/Entity Type
Alternative Medicine
Coding
Coded - Design and coding required
Number of Pages Required
5+ page
Look and feel

```html
<!DOCTYPE html>
<html lang="en">
<head>
<meta charset="utf-8">
<title>Bright Oak Family Medicine</title>
<link rel="stylesheet" href="https://fonts.googleapis.com/css2?family=Playfair+Display:wght@400;700&family=Raleway:wght@400;500;600;700&display=swap">
<style>
:root{
  --green:#7cc51f;
  --green-dark:#5fa70e;
  --blue:#4aa9dc;
  --ink:#2b2b2b;
  --muted:#888;
  --top:#f3f3f3;
  --line:#e4e4e4;
  --footer:#333333;
  --footer-bottom:#232323;
  --white:#fff;
}
*{margin:0;padding:0;box-sizing:border-box}
html,body{width:1200px;height:2703px;overflow:hidden}
body{font-family:'Raleway',sans-serif;color:var(--ink);background:var(--white);position:relative}
.abs{position:absolute}

/* top bar */
.topbar{left:0;top:0;width:1200px;height:100px;background:var(--top)}
.topbar .contact{left:158px;top:40px;font-size:13px;color:#555;display:flex;gap:26px;align-items:center}
.topbar .contact span{display:flex;align-items:center;gap:8px}
.brand{left:0;width:1200px;top:30px;text-align:center}
.brand .name{font-size:30px;font-weight:600;color:var(--ink);display:inline-flex;align-items:center;gap:10px;line-height:36px}
.brand .dot{width:14px;height:14px;border-radius:50%;background:var(--green)}
.login{left:840px;top:40px;font-size:13px;color:#555;display:flex;gap:7px;align-items:center}
.cart{left:915px;top:33px;width:128px;height:31px;border-radius:16px;background:var(--green);color:#fff;font-size:12px;display:flex;align-items:center;justify-content:center;gap:7px}

/* nav */
.nav{left:0;top:100px;width:1200px;height:55px;background:var(--white);border-bottom:1px solid var(--line)}
.nav ul{list-style:none;display:flex;position:absolute;left:158px;top:0;height:55px;align-items:center}
.nav li{font-size:12px;font-weight:500;color:#333;padding:0 13px;height:55px;display:flex;align-items:center}
.nav li.active{background:var(--green);color:#fff;padding:0 14px;height:50px;align-self:flex-start}

/* hero */
.hero{left:0;top:155px;width:1200px;height:355px;background:linear-gradient(180deg,#dbe8ef 0%,#eef3f3 55%,#c9d6a8 82%,#9db66b 100%)}
.hero .photo{right:0;top:0;width:520px;height:355px;background:radial-gradient(ellipse at 60% 55%,#d7b79d 0%,#c7a488 20%,rgba(214,225,225,0) 55%)}
.hero h1{left:154px;top:120px;font-family:'Playfair Display',serif;font-weight:400;font-size:50px;line-height:58px;color:#222}
.hero h1 b{font-weight:700;font-size:52px}
.hero .arrow{top:162px;width:26px;height:26px}

/* sections */
.section-title{left:0;width:1200px;text-align:center;font-family:'Playfair Display',serif;font-weight:400;font-size:30px;color:#222}
.divider{left:540px;width:120px;height:16px}
.tab{width:200px;text-align:center;top:638px}
.tab svg{display:block;margin:0 auto}
.tab .label{font-size:16px;color:#333;margin-top:10px}
.tab.active .label{color:var(--green-dark)}
.svc-line{left:0;top:730px;width:1200px;height:1px;background:var(--line)}
.round{width:22px;height:22px;border-radius:50%;display:flex;align-items:center;justify-content:center}

.feature-img{left:156px;top:763px;width:280px;height:161px;background:linear-gradient(135deg,#c9a184,#e9cdb4 45%,#8fbf6a 100%)}
.feature h3{font-size:19px;font-weight:600;color:#222}
.feature p{font-size:12.5px;line-height:19px;color:#8a8a8a;margin-top:10px}
.btn{display:inline-flex;align-items:center;justify-content:center;border-radius:16px;font-size:11.5px}
.btn.solid{background:var(--green);color:#fff}
.btn.ghost{border:1.5px solid var(--green);color:#333;background:#fff}

/* about */
.about{left:0;top:972px;width:1200px;height:642px;background:linear-gradient(180deg,#4fb0e3 0%,#3fa3d9 70%,#4aaad9 100%);color:#fff;text-align:center}
.about .title{top:42px;left:0;width:1200px;font-family:'Playfair Display',serif;font-size:30px}
.about .sub{top:124px;left:0;width:1200px;font-size:23px;line-height:29px}
.about .body{left:230px;width:740px;top:200px;font-size:13.5px;line-height:19px}
.about .body p{margin-bottom:22px}

/* blog */
.card{top:1813px;width:280px;height:490px;background:#fff;border:1px solid #ececec;text-align:center}
.card.raised{box-shadow:0 0 14px rgba(0,0,0,.15)}
.card .img{position:absolute;left:24px;top:25px;width:232px;height:162px}
.card .date{position:absolute;left:90px;top:171px;width:100px;height:24px;background:var(--green);color:#fff;font-size:11.5px;display:flex;align-items:center;justify-content:center}
.card h4{position:absolute;left:0;width:100%;top:215px;font-size:18px;font-weight:600;line-height:21px;color:#222}
.card p{position:absolute;left:40px;width:200px;top:268px;font-size:12.5px;line-height:18px;color:#8a8a8a}
.card .meta{position:absolute;left:0;width:100%;top:378px;font-size:11.5px;color:#888;display:flex;justify-content:center;gap:14px}
.card .meta span{display:flex;align-items:center;gap:5px}
.card .btn{position:absolute;left:90px;top:435px;width:98px;height:32px}

/* footer */
.footer{left:0;top:2352px;width:1200px;height:300px;background:var(--footer);color:#ddd}
.footer h5{font-size:16px;font-weight:600;color:#fff}
.footer .col{top:45px}
.footer .row{display:flex;gap:14px;font-size:12px;line-height:17px;color:#ccc}
.footer ul{list-style:none;margin-top:20px}
.footer li{font-size:12.5px;line-height:19.3px;color:#ccc}
.footer li::before{content:"» ";color:var(--green)}
.footer li.on{color:var(--green)}
.hours td{font-size:12.5px;line-height:19.3px;color:#ccc;padding-right:40px}
.field{width:202px;height:31px;border:1px solid #666;border-radius:16px;font-size:11px;color:#888;padding:0 14px;display:flex;align-items:center}
.social{width:24px;height:24px;border-radius:50%;border:1.5px solid #bbb}
.bottom{left:0;top:2652px;width:1200px;height:51px;background:var(--footer-bottom);color:#ccc;font-size:12px}
</style>
</head>
<body>

<header class="abs topbar">
  <div class="abs contact">
    <span><svg width="13" height="13" viewBox="0 0 24 24"><path d="M6.6 10.8a15 15 0 0 0 6.6 6.6l2.2-2.2c.3-.3.7-.4 1-.2 1.1.4 2.3.6 3.6.6.6 0 1 .4 1 1V20c0 .6-.4 1-1 1C10.6 21 3 13.4 3 4c0-.6.4-1 1-1h3.5c.6 0 1 .4 1 1 0 1.3.2 2.5.6 3.6.1.3 0 .7-.2 1z" fill="#7cc51f"/></svg>(555) 014-2380</span>
    <span><svg width="13" height="11" viewBox="0 0 24 18"><rect x="1" y="1" width="22" height="16" rx="2" fill="none" stroke="#7cc51f" stroke-width="2"/><path d="M1 2l11 8 11-8" fill="none" stroke="#7cc51f" stroke-width="2"/></svg>info@brightoakfm.com</span>
  </div>
  <div class="abs brand">
    <div class="name"><span class="dot"></span>Bright Oak</div>
  </div>
  <div class="abs login"><svg width="12" height="13" viewBox="0 0 24 24"><circle cx="12" cy="7" r="5" fill="#7cc51f"/><path d="M2 23c0-6 4.5-9 10-9s10 3 10 9z" fill="#7cc51f"/></svg>Login</div>
  <div class="abs cart"><svg width="12" height="12" viewBox="0 0 24 24"><path d="M3 4h3l3 11h10l3-8H8" fill="none" stroke="#fff" stroke-width="2"/><circle cx="10" cy="20" r="2" fill="#fff"/><circle cx="18" cy="20" r="2" fill="#fff"/></svg>Item $0.00</div>
</header>

<nav class="abs nav">
  <ul>
    <li class="active">Home</li><li>About us</li><li>Services</li><li>Resources</li><li>FAQ</li><li>Current Patients</li><li>New Patients</li><li>OakWell Membership</li><li>Contact us</li>
    <li><svg width="13" height="13" viewBox="0 0 24 24"><circle cx="10" cy="10" r="7" fill="none" stroke="#333" stroke-width="3"/><path d="M15 15l7 7" stroke="#333" stroke-width="3"/></svg></li>
    <li><svg width="13" height="12" viewBox="0 0 24 20"><path d="M2 3h20M2 10h20M2 17h20" stroke="#333" stroke-width="3"/></svg></li>
  </ul>
</nav>

<section class="abs hero">
  <div class="abs photo" role="img" aria-label="Cupped hands holding a small tree seedling against a sky and meadow"></div>
  <h1 class="abs">Helping you to live a<br><b>Bright Life</b></h1>
  <svg class="abs arrow" style="left:80px" viewBox="0 0 26 26"><rect x="1" y="1" width="24" height="24" fill="none" stroke="#333" stroke-width="1.2"/><path d="M16 7l-6 6 6 6" fill="none" stroke="#333" stroke-width="1.5"/></svg>
  <svg class="abs arrow" style="left:1090px" viewBox="0 0 26 26"><rect x="1" y="1" width="24" height="24" fill="none" stroke="#fff" stroke-width="1.2"/><path d="M10 7l6 6-6 6" fill="none" stroke="#fff" stroke-width="1.5"/></svg>
</section>

<h2 class="abs section-title" style="top:550px">Our Services</h2>
<svg class="abs divider" style="top:596px" viewBox="0 0 120 16"><path d="M0 8h48M72 8h48" stroke="#7cc51f" stroke-width="1.5"/></svg>

<div class="abs round" style="left:109px;top:675px;border:1px solid #ccc"><svg width="8" height="8" viewBox="0 0 8 8"><path d="M6 0L2 4l4 4" fill="none" stroke="#333" stroke-width="1.5"/></svg></div>
<div class="abs round" style="left:1067px;top:675px;background:var(--green)"><svg width="8" height="8" viewBox="0 0 8 8"><path d="M2 0l4 4-4 4" fill="none" stroke="#fff" stroke-width="1.5"/></svg></div>

<div class="abs tab active" style="left:157px">
  <svg width="50" height="42" viewBox="0 0 50 42" fill="none" stroke="#7cc51f" stroke-width="2"><circle cx="15" cy="9" r="6"/><circle cx="35" cy="9" r="6"/><circle cx="25" cy="22" r="4"/><path d="M4 40V26a11 11 0 0 1 11-10M46 40V26a11 11 0 0 0-11-10M18 40v-6a7 7 0 0 1 14 0v6"/></svg>
  <div class="label">Family Medicine</div>
</div>
<div class="abs tab" style="left:386px">
  <svg width="46" height="42" viewBox="0 0 46 42" fill="none" stroke="#333" stroke-width="2"><rect x="8" y="2" width="30" height="26" rx="2"/><path d="M2 30h42a21 11 0 0 1-42 0z"/><circle cx="23" cy="15" r="6"/></svg>
  <div class="label">Nutrition</div>
</div>
<div class="abs tab" style="left:613px">
  <svg width="46" height="42" viewBox="0 0 46 42" fill="none" stroke="#333" stroke-width="2"><path d="M10 2l16 36M20 2l10 36M34 4l-4 34M6 38h34"/></svg>
  <div class="label">Acupuncture</div>
</div>
<div class="abs tab" style="left:841px">
  <svg width="46" height="42" viewBox="0 0 46 42" fill="none" stroke="#333" stroke-width="2"><path d="M23 2v38M14 8h18M11 15h24M13 22h20M15 29h16M17 36h12"/></svg>
  <div class="label">Prolotherapy</div>
</div>
<div class="abs svc-line"></div>

<div class="abs feature-img" role="img" aria-label="Smiling family of four posing together outdoors"></div>
<div class="abs feature" style="left:459px;top:758px;width:585px">
  <h3>Family Medicine</h3>
  <p>In addition to what you would expect from any family medicine clinic, we utilize many different modalities in our attempt to improve your quality of health, whether it is pharmaceutical or nutraceutical. Routine primary care is provided for newborns to adults. We do everything that a primary care practice does plus we deliver it in an integrative way....</p>
  <span class="btn solid" style="width:97px;height:31px;margin-top:14px">Read More</span>
</div>

<section class="abs about">
  <div class="abs title">About Us</div>
  <svg class="abs" style="left:540px;top:88px;width:120px;height:16px" viewBox="0 0 120 16"><path d="M0 8h48M72 8h48" stroke="#fff" stroke-width="1.5"/></svg>
  <div class="abs sub">Restoring your Health Naturally with<br>Nutrition, Manipulation, Acupuncture, and Integrative Medicine</div>
  <div class="abs body">
    <p>Welcome to our website. As an integrative medical practice, we provide innovative, quality family health care by uniquely combining both conventional and alternative medicine. Our aim is to treat the whole patient not just the symptoms. This "best of both worlds" approach provides patients with options in the management of their concerns while addressing the underlying cause of their illness. And as a primary care practice, we offer treatment for both acute and chronic conditions while emphasizing prevention, education and optimal health.</p>
    <p style="font-size:12px;line-height:18px">In our practice, we believe prevention is the key to lifelong health and wellness. We are committed to helping you get well, stay well and live well. It is our mission not only to heal, but to inspire and motivate our patients to embrace and follow a path leading to wellness and a healthy long life.</p>
    <p>At the heart of this practice, though, is the partnership between doctor and patient in the process of healing. Our staff is dedicated to providing high-quality, individualized and compassionate care to patients of all ages We aim to thoroughly educate you about your medical condition, while accommodating your unique needs and providing you with a positive and satisfying experience.</p>
    <p style="font-size:12px;line-height:18px">This website is just one of the many ways we hope to teach and inspire you towards embracing your full health potential. As you navigate through the site, you will find a wealth of information about our practice and the treatments we offer. We hope that you find the website informative and invite you to call our office with questions and/or to schedule an appointment. We look forward to meeting you and to guiding you along the way to a healthier, more comfortable lifestyle.</p>
  </div>
</section>

<span class="abs btn solid" style="left:308px;top:1646px;width:280px;height:32px;font-size:12px">Schedule a Free Nutrition Counselling</span>
<span class="abs btn ghost" style="left:611px;top:1646px;width:281px;height:32px;font-size:12px">Are you toxic questionnaire?</span>

<h2 class="abs section-title" style="top:1716px">Our Blog</h2>
<svg class="abs divider" style="top:1762px" viewBox="0 0 120 16"><path d="M0 8h48M72 8h48" stroke="#7cc51f" stroke-width="1.5"/></svg>

<article class="abs card" style="left:156px">
  <div class="img" role="img" aria-label="Happy couple embracing at the beach" style="background:linear-gradient(135deg,#dfeef7,#e8c8ab 55%,#cfe3ef)"></div>
  <div class="date">25 Oct, 2016</div>
  <h4>The standard Lorem<br>Ipsum passage</h4>
  <p>There are many variations of passages of Lorem Ipsum available, but the majority have suffered alteration in some form...</p>
  <div class="meta"><span>&#9679; Lorem</span><span>&#9675; 30 Comment</span><span>&#8918; Share</span></div>
  <span class="btn ghost">Read More</span>
</article>
<article class="abs card raised" style="left:460px">
  <div class="img" role="img" aria-label="Smiling senior couple standing together" style="background:linear-gradient(135deg,#cfe5f3,#e6d2c2 50%,#f1f1f1)"></div>
  <div class="date">20 Sep, 2016</div>
  <h4>The standard Lorem<br>Ipsum passage</h4>
  <p>There are many variations of passages of Lorem Ipsum available, but the majority have suffered alteration in some form...</p>
  <div class="meta"><span>&#9679; Lorem</span><span>&#9675; 30 Comment</span><span>&#8918; Share</span></div>
  <span class="btn solid">Read More</span>
</article>
<article class="abs card" style="left:764px">
  <div class="img" role="img" aria-label="Therapist giving a back massage" style="background:linear-gradient(135deg,#f3ece6,#d9b08f 55%,#c28e6a)"></div>
  <div class="date">25 Dec, 2016</div>
  <h4>The standard Lorem<br>Ipsum passage</h4>
  <p>There are many variations of passages of Lorem Ipsum available, but the majority have suffered alteration in some form...</p>
  <div class="meta"><span>&#9679; Lorem</span><span>&#9675; 30 Comment</span><span>&#8918; Share</span></div>
  <span class="btn ghost">Read More</span>
</article>

<footer class="abs footer">
  <div class="abs col" style="left:156px;width:200px">
    <h5>Contact Us</h5>
    <div class="row" style="margin-top:20px"><svg width="12" height="16" viewBox="0 0 12 16"><path d="M6 0a6 6 0 0 0-6 6c0 4 6 10 6 10s6-6 6-10a6 6 0 0 0-6-6z" fill="#ccc"/><circle cx="6" cy="6" r="2" fill="#333"/></svg><span>418 Meadow Lane, Fairview,<br>TX 75000</span></div>
    <div class="row" style="margin-top:18px"><svg width="12" height="14" viewBox="0 0 24 24"><path d="M6.6 10.8a15 15 0 0 0 6.6 6.6l2.2-2.2c.3-.3.7-.4 1-.2 1.1.4 2.3.6 3.6.6.6 0 1 .4 1 1V20c0 .6-.4 1-1 1C10.6 21 3 13.4 3 4c0-.6.4-1 1-1h3.5c.6 0 1 .4 1 1 0 1.3.2 2.5.6 3.6.1.3 0 .7-.2 1z" fill="#ccc"/></svg><span>Phone: (555) 014-2380<br>Fax: (555) 014-2391</span></div>
    <div class="row" style="margin-top:18px"><svg width="13" height="11" viewBox="0 0 24 18"><rect x="1" y="1" width="22" height="16" rx="2" fill="#ccc"/><path d="M1 2l11 8 11-8" fill="none" stroke="#333" stroke-width="2"/></svg><span>info@brightoakfm.com</span></div>
    <div style="display:flex;gap:12px;margin-top:22px">
      <span class="social"></span><span class="social" style="background:var(--green);border-color:var(--green)"></span><span class="social"></span>
    </div>
  </div>
  <div class="abs col" style="left:383px">
    <h5>Quick Links</h5>
    <ul>
      <li class="on">Home</li><li>About us</li><li>Services</li><li>Resources</li><li>FAQ</li><li>Current Patients</li><li>New Patients</li><li>OakWell Membership</li><li>Contact us</li>
    </ul>
  </div>
  <div class="abs col" style="left:586px">
    <h5>Working Hours</h5>
    <table class="hours" style="margin-top:20px;border-collapse:collapse">
      <tr><td>Monday :</td><td>8 am - 6 pm</td></tr>
      <tr><td>Tuesday :</td><td>8 am - 6 pm</td></tr>
      <tr><td>Wednesday :</td><td>9 am - 6 pm</td></tr>
      <tr><td>Thursday :</td><td>8 am - 4 pm</td></tr>
      <tr><td>Friday :</td><td>9 am - 1 pm</td></tr>
    </table>
    <div style="color:var(--green);font-size:12.5px;line-height:19px;margin-top:18px">The office is closed from<br>12-1 for lunch</div>
  </div>
  <div class="abs col" style="left:839px">
    <h5>Newsletter</h5>
    <div class="field" style="margin-top:20px">Name :</div>
    <div class="field" style="margin-top:14px">Email :</div>
    <span class="btn solid" style="width:96px;height:31px;margin-top:14px;gap:6px"><svg width="11" height="11" viewBox="0 0 24 24"><path d="M2 12L22 2l-6 20-4-8z" fill="#fff"/></svg>Send</span>
  </div>
</footer>

<div class="abs bottom">
  <span class="abs" style="left:156px;top:18px">© 2016 Bright Oak Family Medicine.</span>
  <div class="abs round" style="left:1016px;top:14px;width:24px;height:24px;background:var(--green)"><svg width="10" height="8" viewBox="0 0 10 8"><path d="M1 7l4-5 4 5" fill="none" stroke="#fff" stroke-width="1.8"/></svg></div>
</div>

</body>
</html>
```